Tendril Harbor

Our product is a subscription-based website for doctors and medical practices. It allows contract-based doctors (locums) to book jobs with medical practices and to organise their own finances (invoicing, pension, etc). Also, it allows medical practices to post jobs, and book locums.

We need a website design that looks clean and professional. It should look easy-to-use and friendly, which will encourage users to sign up as they'll hopefully think using the system will also be simple and friendly.

As well as the homepage, we need a design for the logged-in view. This is very different to the website but equally important. It needs to be very functional. Much more like an application and less like a website.

PLEASE SUBMIT BOTH WEBSITE HOMEPAGE DESIGN AND APPLICATION DASHBOARD DESIGN.

The application is built and we already have a user interface (linked below) so we're not looking for a designer to decide what is on these pages - we already have that. We're ONLY asking for visual design. Please just make the content we have look good. You may move parts of the content around a small amount but the functionality is very much signed off now so it's only visual styling that we need addressed.

Please base the branding around the current logo, which can't be changed. You can get the logo as an EPS here : http://clients.brassowl.co.uk/tendrilharbor/design/logo-green.eps

Here is a link to the current design for the website, and for the application dashboard:
http://clients.brassowl.co.uk/tendrilharbor/design/

Also, here is a video we've had made which might help you with the brand:
http://quivlo.com/71825364
Updates

Just in case it isn't clear, the video (LinkUp Pro the main brief) is an essential part of the website homepage.

Reason: We need to spend some time looking over these designs and might ask for a few amendments to one or two in the next few days. Thanks.

Target Market(s)

Doctors and medical practices

Industry/Entity Type

Medical

Requirements
Must have
• It must have all the features that are in the linked designs - homepage and dashboard.

```html
<!DOCTYPE html>
<html lang="en">
<head>
<meta charset="utf-8">
<title>Tendril Harbor – Home</title>
<link href="https://fonts.googleapis.com/css2?family=Ubuntu:ital,wght@0,400;0,500;0,700;1,400;1,500&display=swap" rel="stylesheet">
<style>
:root{
  --dark:#363636;
  --footer:#333333;
  --page:#eeeeee;
  --green:#86ad2c;
  --green-dark:#6a8f1b;
  --green-text:#7ea425;
  --blue:#5a8ec3;
  --blue-dark:#3f73a8;
  --blue-text:#3d6fa3;
  --text:#444444;
  --muted:#8a8a8a;
  --white:#ffffff;
  --card:#f7f7f7;
  --line:#d8d8d8;
}
*{margin:0;padding:0;box-sizing:border-box}
html,body{width:733px;height:1200px;overflow:hidden}
body{position:relative;background:var(--page);font-family:"Ubuntu",sans-serif;color:var(--text);font-size:9px}
.abs{position:absolute}

.topbar{left:0;top:0;width:733px;height:30px;background:var(--dark);box-shadow:0 1px 3px rgba(0,0,0,.4)}
.welcome{right:78px;top:9px;color:var(--white);font-size:8.5px;font-weight:500;display:flex;gap:6px;align-items:center;white-space:nowrap}
.welcome .name{color:var(--green)}
.dash-btn{background:var(--blue);border:1px solid #8fb6de;border-radius:3px;padding:2px 5px;color:var(--white)}

.brand{left:0;top:42px;width:733px;display:flex;justify-content:center;align-items:center;gap:10px}
.brand-mark{width:46px;height:46px;border-radius:50%;background:var(--blue-dark)}
.brand-name{font-size:22px;font-weight:500;color:var(--blue-dark);line-height:1}
.header-rule{left:79px;top:100px;width:575px;height:2px;background:linear-gradient(90deg,transparent,#ccc,transparent)}

.nav{left:79px;top:114px;width:575px;height:28px;background:linear-gradient(#98bd3c,#74991f);border-radius:3px;border-bottom:2px solid #5d7e14;display:flex;justify-content:space-around;align-items:center;color:var(--white);font-size:8.5px;font-weight:500}

.hero{left:0;top:152px;width:733px;height:246px;background:linear-gradient(#6c9ccf,var(--blue) 60%,#4f83ba)}
.video{left:79px;top:19px;width:330px;height:186px;border:3px solid var(--white);background:radial-gradient(circle at 50% 45%,#e4f6fb,#9fd6e8 70%,#7ec3dc);box-shadow:0 8px 14px rgba(0,0,0,.25)}
.video-bar{left:0;bottom:0;width:100%;height:14px;background:#2b2b2b}
.video-url{left:0;bottom:17px;width:100%;text-align:center;color:var(--blue-dark);font-size:9px}
.hero h1{left:433px;top:16px;width:240px;color:var(--white);font-size:17px;font-weight:500;line-height:21.5px;letter-spacing:.3px;white-space:nowrap}
.ticks{left:433px;top:60px;list-style:none;color:var(--white);font-size:10px;font-weight:500}
.ticks li{height:21.5px;display:flex;align-items:center;gap:8px;white-space:nowrap}
.cta{left:511px;top:176px;width:142px;height:30px;background:linear-gradient(#94bb36,#75991f);border-bottom:2px solid #55740f;border-radius:2px;color:var(--white);font-size:9.5px;font-weight:500;display:flex;align-items:center;justify-content:center;white-space:nowrap}
.dots{left:603px;top:226px;display:flex;gap:4px}
.dots span{width:10px;height:10px;border-radius:50%;background:rgba(255,255,255,.55)}
.dots span:first-child{background:var(--white)}

.pill{top:413px;width:281px;height:22px;border-radius:11px;color:var(--white);font-size:11.5px;font-weight:500;padding-left:34px;line-height:22px}
.pill.green{left:79px;background:linear-gradient(#93ba35,#76991f)}
.pill.blue{left:373px;background:linear-gradient(#6e9dcf,#4c80b6)}
.lede{top:447px;font-size:9px}

.card{width:281px;height:50px;background:var(--card);border:1px solid #e2e2e2;box-shadow:0 1px 2px rgba(0,0,0,.08);padding:6px 6px 0 40px}
.card .num{left:6px;top:10px;width:28px;height:28px;border-radius:50%;background:#6d6d6d;color:var(--white);font-size:15px;display:flex;align-items:center;justify-content:center}
.card h3{font-size:10px;font-style:italic;font-weight:500;margin-bottom:2px;white-space:nowrap}
.card p{font-size:7.8px;line-height:12px}
.col-left .card h3{color:var(--green-text)}
.col-right .card h3{color:var(--blue-text)}
.btn{height:23px;width:67px;border-radius:2px;color:var(--white);font-size:9.5px;font-weight:500;display:flex;align-items:center;justify-content:center}
.btn.green{background:linear-gradient(#94bb36,#75991f)}
.btn.blue{background:linear-gradient(#6e9dcf,#4c80b6)}
.divider{left:79px;top:683px;width:575px;height:2px;background:linear-gradient(90deg,transparent,#ccc 15%,#ccc 85%,transparent)}

.step{top:702px;width:182px;height:46px;border-radius:23px;background:linear-gradient(#848484,#5c5c5c);color:var(--white);display:flex;align-items:center}
.step .big{font-size:40px;font-weight:700;color:rgba(255,255,255,.18);width:42px;text-align:center;margin-left:4px}
.step .label{font-size:10px;font-style:italic;font-weight:500;line-height:15px;flex:1}

.says{left:79px;top:767px;font-size:13px;font-weight:500;color:#444}
.press{left:79px;width:119px;height:41px;background:var(--white);border:1px solid #d5d5d5;display:flex;align-items:center;justify-content:center;font-size:12px;font-weight:700;color:#1d3c6e}
.quote{left:205px;width:155px;font-size:7.4px;font-style:italic;line-height:12.5px;color:#555;padding:2px 0 0 14px}
.quote .qo,.quote .qc{position:absolute;font-family:Georgia,serif;font-size:32px;color:var(--blue);font-style:normal;line-height:1}
.quote .qo{left:0;top:-6px}
.quote .qc{left:66px;bottom:-24px}
.vrule{left:366px;top:765px;width:1px;height:228px;background:var(--line)}
.try{left:383px;top:770px;width:130px;font-size:11.5px;font-style:italic;font-weight:500;line-height:14.5px;color:#333}
.photo{left:522px;top:767px;width:131px;height:97px;background:linear-gradient(135deg,#e8e2d8,#cfd7dc 55%,#b8a792);border:1px solid #ccc}
.iam{left:383px;top:869px;font-size:7.8px;display:flex;align-items:center;gap:5px;white-space:nowrap}
.radio{width:9px;height:9px;border-radius:50%;border:1px solid #999;background:var(--white);display:inline-block;position:relative}
.radio.on::after{content:"";position:absolute;left:2px;top:2px;width:3px;height:3px;border-radius:50%;background:var(--blue)}
.field{width:123px;height:18px;background:var(--white);border:1px solid #ccc;border-radius:2px;font-size:7.5px;color:#777;padding:4px 7px}
.agree{left:383px;top:948px;font-size:7.5px;display:flex;align-items:center;gap:6px;white-space:nowrap}
.agree .box{width:8px;height:8px;border:1px solid #aaa;background:var(--white)}
.agree a{color:var(--blue-text);text-decoration:none}

.footer{left:0;top:1007px;width:733px;height:193px;background:var(--footer);color:#cfcfcf}
.testi{top:22px;width:200px;font-size:9px;font-style:italic;line-height:15px}
.testi .who{display:block;margin-top:9px;color:#6f9ccd;font-size:7.8px}
.follow{left:546px;top:22px;font-size:9.5px;font-weight:500;color:var(--white)}
.social{left:546px;top:42px;list-style:none;font-size:7.6px}
.social li{height:17.5px;display:flex;align-items:center;gap:7px}
.social i{width:9px;height:9px;display:inline-block;border-radius:1px}
.f-rule{left:79px;top:111px;width:428px;height:1px;background:#555}
.f-links{left:79px;top:125px;font-size:8px;font-weight:500;color:var(--green);white-space:nowrap}
.f-links span{color:#aaa;margin:0 5px}
.f-info{left:79px;top:140px;font-size:7.4px;line-height:15.5px;color:#b5b5b5;white-space:nowrap}
.legal{right:79px;top:171px;font-size:7.4px;color:#b5b5b5;white-space:nowrap}
.legal span{margin:0 4px}
</style>
</head>
<body>

<div class="abs topbar">
  <div class="abs welcome">Welcome <span class="name">Mr. Tobias Wrenfield</span> <span class="dash-btn">Go to Dashboard</span> Sign-Out</div>
</div>

<header class="abs brand">
  <span class="brand-mark"></span>
  <span class="brand-name">Tendril Harbor</span>
</header>
<div class="abs header-rule"></div>

<nav class="abs nav">
  <span>Home</span><span>Locums</span><span>Employers</span><span>Pricing</span><span>About Us</span><span>FAQ</span><span>Contact Us</span>
</nav>

<section class="abs hero">
  <div class="abs video" role="img" aria-label="Introductory video player showing the Tendril Harbor title frame">
    <div class="abs video-url">www.TendrilHarbor.co.uk</div>
    <div class="abs video-bar">
      <svg width="330" height="14"><polygon points="10,3 10,11 17,7" fill="#fff"/><rect x="30" y="5" width="260" height="4" fill="#555"/><rect x="30" y="5" width="6" height="4" fill="#9bd"/></svg>
    </div>
  </div>
  <h1 class="abs">A Network &nbsp;for Connecting<br>Locums with Employers</h1>
  <ul class="abs ticks">
    <li><svg width="9" height="8"><path d="M1 4 L3.5 7 L8 1" stroke="#fff" stroke-width="1.8" fill="none"/></svg>Better Connectivity</li>
    <li><svg width="9" height="8"><path d="M1 4 L3.5 7 L8 1" stroke="#fff" stroke-width="1.8" fill="none"/></svg>More Choice</li>
    <li><svg width="9" height="8"><path d="M1 4 L3.5 7 L8 1" stroke="#fff" stroke-width="1.8" fill="none"/></svg>Less Paperwork</li>
    <li><svg width="9" height="8"><path d="M1 4 L3.5 7 L8 1" stroke="#fff" stroke-width="1.8" fill="none"/></svg>Lower Costs</li>
  </ul>
  <div class="abs cta">SignUp for FREE- try us out</div>
  <div class="abs dots"><span></span><span></span><span></span><span></span></div>
</section>

<div class="abs pill green">GP Locums</div>
<div class="abs pill blue">Employers</div>
<p class="abs lede" style="left:80px">The complete platform to orgnise your locums life.</p>
<p class="abs lede" style="left:373px">One -step solution for your locum need</p>

<div class="col-left">
  <div class="abs card" style="left:79px;top:471px"><span class="abs num">1</span><h3>Find Locum</h3><p>Aliquam molestie, mi et imperdiet euismod, dui purus auctor tellus, et interdum lacus lectus et ante.</p></div>
  <div class="abs card" style="left:79px;top:527px"><span class="abs num">2</span><h3>Do your locums admin easily online</h3><p>Aliquam molestie, mi et imperdiet euismod, dui purus auctor tellus, et interdum lacus lectus et ante.</p></div>
  <div class="abs card" style="left:79px;top:585px"><span class="abs num">2</span><h3>Create and grow your &nbsp;“locum network”</h3><p>Aliquam molestie, mi et imperdiet euismod, dui purus auctor tellus, et interdum lacus lectus et ante.</p></div>
  <div class="abs btn green" style="left:186px;top:648px">SignUp</div>
</div>
<div class="col-right">
  <div class="abs card" style="left:373px;top:471px"><span class="abs num">1</span><h3>Find Jobs</h3><p>Aliquam molestie, mi et imperdiet euismod, dui purus auctor tellus, et interdum lacus lectus et ante.</p></div>
  <div class="abs card" style="left:373px;top:527px"><span class="abs num">2</span><h3>Do your locums admin easily online</h3><p>Aliquam molestie, mi et imperdiet euismod, dui purus auctor tellus, et interdum lacus lectus et ante.</p></div>
  <div class="abs card" style="left:373px;top:585px"><span class="abs num">2</span><h3>Create and grow your &nbsp;“employers network”</h3><p>Aliquam molestie, mi et imperdiet euismod, dui purus auctor tellus, et interdum lacus lectus et ante.</p></div>
  <div class="abs btn blue" style="left:480px;top:648px">SignUp</div>
</div>

<div class="abs divider"></div>

<div class="abs step" style="left:79px"><span class="big">1</span><span class="label">The “network” for<br>locums &amp; employers</span><svg width="34" height="14"><path d="M4 7 H20 M15 2 L22 7 L15 12" stroke="#9cc43a" stroke-width="3" fill="none"/></svg></div>
<div class="abs step" style="left:276px"><span class="big">2</span><span class="label">Save time &amp; cost</span><svg width="34" height="14"><path d="M4 7 H20 M15 2 L22 7 L15 12" stroke="#9cc43a" stroke-width="3" fill="none"/></svg></div>
<div class="abs step" style="left:471px"><span class="big">3</span><span class="label">Try it free now !</span></div>

<h2 class="abs says">What Other Says...</h2>
<div class="abs press" style="top:797px">Morning Ledger</div>
<div class="abs press" style="top:865px">Daily Courier</div>
<div class="abs press" style="top:934px">The Dispatch</div>
<p class="abs quote" style="top:794px"><span class="qo">“</span>Lorem ipsum dolor sit amet, consectetur adipiscing elit. Fusce accumsan, elit a suscipit sagittis.....<span class="qc">”</span></p>
<p class="abs quote" style="top:862px"><span class="qo">“</span>Lorem ipsum dolor sit amet, consectetur adipiscing elit. Fusce accumsan, elit a suscipit sagittis.....<span class="qc">”</span></p>
<p class="abs quote" style="top:931px"><span class="qo">“</span>Lorem ipsum dolor sit amet, consectetur adipiscing elit. Fusce accumsan, elit a suscipit sagittis.....<span class="qc">”</span></p>

<div class="abs vrule"></div>

<p class="abs try">Try it now just an email address, GMC number and password !</p>
<div class="abs photo" role="img" aria-label="Photo of a doctor talking with a smiling older patient"></div>
<div class="abs iam">I am <span class="radio on"></span> a locum <span class="radio"></span> an employers</div>
<div class="abs field" style="left:383px;top:891px">Email:</div>
<div class="abs field" style="left:519px;top:891px">GMC Number</div>
<div class="abs field" style="left:383px;top:921px">Password</div>
<div class="abs field" style="left:519px;top:921px">Confirm Password</div>
<div class="abs agree"><span class="box"></span><span>I agree to the <a>terms of services</a> and the <a>privacy policy</a></span></div>
<div class="abs btn green" style="left:576px;top:970px">SignUp</div>

<footer class="abs footer">
  <p class="abs testi" style="left:79px">Nam fermentum vestibulum purus id aliquet. Phasellus dui ante, ultricies et sollicitudin pretium, fermentum vel velit.....<span class="who">Name of the person, Locum</span></p>
  <p class="abs testi" style="left:323px">Nam fermentum vestibulum purus id aliquet. Phasellus dui ante, ultricies et sollicitudin pretium, fermentum vel velit.....<span class="who">Blah Medical Centre</span></p>
  <h4 class="abs follow">Follow Us On:</h4>
  <ul class="abs social">
    <li><i style="background:#3b5b98"></i>Friendwall</li>
    <li><i style="background:#3fa3d8"></i>Chirper</li>
    <li><i style="background:#2a71a8"></i>LinkUp Pro</li>
    <li><i style="background:#e8821e"></i>Rss Feed</li>
    <li><i style="background:#3aa9cf"></i>Clipreel</li>
  </ul>
  <div class="abs f-rule"></div>
  <div class="abs f-links">Home<span>|</span>Locums<span>|</span>Employers<span>|</span>About Us<span>|</span>FAQ<span>|</span>Contact Us</div>
  <p class="abs f-info">We're here to help:help@tendrilharbor.co.uk<br>Copyright © 2013 Tendril Harbor Ltd.. All Right Reserved<br>Registered in England no: 08815237</p>
  <p class="abs legal">Term of services<span>|</span>Privacy Policy<span>|</span>Refund Policy</p>
</footer>

</body>
</html>
```